Luxury Wine Label for New Startup Winery

We need a wine label for our new winery startup. We have worked with a local designer but do not feel the resulting label / logo have the elevation required to present our brand as a luxury wine. Our winery is called "Harrowgate Vineyards" and we are focused on extremely high quality hand crafted artisan and estate wines from the Pacific Northwest.
We would like to see designs that utilize a tree line, or other imagery that represents the "Harrowgate" part of our company name. Another interesting feature could be wood grain.
A logo will be required based on your design so please design with this in mind:
This logo should be consistent with the wine bottle label design, and should be representative of our high end exclusive wine while giving a sense of place (Oregon/ Pacific Northwest.)
I will supply an image of the design we received from our local designer, PLEASE NOTE: in general we do like wood grain and tree line concepts but feel the execution was poorly done.
ATTN: Logo design should be suitable for use on: Bottles (Red wine/rose/white wine), Bussiness cards, vehicle signage, business signage, etc
P.S.:
If you have a design that is not outside the box we are still interested in seeing it.
Label is for a burgundy style bottle with a label height of 3.5 - 4" and a width of 3.5-4"
any label <= 4"x4" and >=3.5"x3.5" will be acceptable:
HOWEVER Width should be greater than or equal to height due to the bottle format
Target Market(s)
Wine enthusiasts with adequate discretionary budgets to afford $100 bottles of wine.
Industry/Entity Type
Wine / Winery
Requirements
Must have
- A sense of luxury, a feel of exclusivity, and a theme consistent with our product and brand name
Nice to have
- Tree line, wood grain or other wood themes. Serif fonts
Should not have
- anything cheesy, off topic, hard to read script fonts or anything that makes the label hard to read from a few feet away or too busy

```html
<!DOCTYPE html>
<html lang="en">
<head>
<meta charset="utf-8">
<title>Harrowgate Vineyards — Label Set</title>
<link href="https://fonts.googleapis.com/css2?family=Cinzel:wght@400;500&family=Cormorant+Garamond:wght@400;500&family=Pinyon+Script&display=swap" rel="stylesheet">
<style>
  :root {
    --backdrop: #2a2a2c;
    --rose-paper: #eeeeee;
    --rose-ink: #4a4a4a;
    --rose-accent: #b3262c;
    --rose-grain-hi: #e3e3e3;
    --rose-grain-lo: #cfcfcf;
    --syrah-paper: #1b1b1c;
    --syrah-ink: #c9c9c9;
    --syrah-grain-hi: #2c2c2e;
    --syrah-grain-lo: #141415;
  }
  * { margin: 0; padding: 0; box-sizing: border-box; }
  html, body { width: 1200px; height: 900px; overflow: hidden; }
  body {
    background: var(--backdrop);
    position: relative;
    font-family: "Cormorant Garamond", serif;
  }
  .label {
    position: absolute;
    top: 230px;
    width: 440px;
    height: 420px;
    overflow: hidden;
    box-shadow: 0 20px 50px rgba(0,0,0,0.45);
  }
  .label--rose { left: 100px; background: var(--rose-paper); color: var(--rose-ink); }
  .label--syrah { left: 660px; background: var(--syrah-paper); color: var(--syrah-ink); }

  .wood-grain {
    position: absolute;
    border-radius: 48% 52% 40% 60% / 55% 45% 55% 45%;
  }
  .label--rose .wood-grain {
    left: 160px; top: -30px; width: 300px; height: 300px;
    background: radial-gradient(ellipse at 60% 70%, var(--rose-grain-lo), var(--rose-grain-hi) 60%, transparent 75%);
  }
  .label--syrah .wood-grain {
    left: 40px; top: -40px; width: 400px; height: 280px;
    background: radial-gradient(ellipse at 55% 65%, var(--syrah-grain-hi), var(--syrah-grain-lo) 60%, transparent 78%);
  }

  .wordmark {
    position: absolute;
    font-family: "Cinzel", serif;
    font-weight: 500;
    letter-spacing: 0.04em;
  }
  .subline {
    position: absolute;
    display: flex;
    align-items: center;
    gap: 10px;
    font-family: "Cinzel", serif;
    letter-spacing: 0.35em;
  }
  .subline .rule { height: 1px; background: currentColor; opacity: 0.7; }
  .varietal { position: absolute; font-family: "Pinyon Script", cursive; }
  .region { position: absolute; letter-spacing: 0.08em; }
  .vintage {
    position: absolute;
    font-family: "Cinzel", serif;
    letter-spacing: 0.22em;
  }

  /* Rosé label: left-aligned block */
  .label--rose .wordmark { left: 36px; top: 258px; font-size: 36px; }
  .label--rose .subline { left: 38px; top: 304px; font-size: 13px; }
  .label--rose .subline .rule { width: 150px; }
  .label--rose .varietal { left: 36px; top: 318px; font-size: 38px; color: var(--rose-accent); }
  .label--rose .region { left: 38px; top: 368px; font-size: 17px; }
  .label--rose .vintage { left: 38px; top: 394px; font-size: 9px; }

  /* Syrah label: centred block */
  .label--syrah .wordmark,
  .label--syrah .region,
  .label--syrah .varietal,
  .label--syrah .vintage { left: 0; right: 0; text-align: center; }
  .label--syrah .wordmark { top: 176px; font-size: 36px; }
  .label--syrah .subline { left: 0; right: 0; top: 222px; justify-content: center; font-size: 13px; }
  .label--syrah .subline .rule { width: 70px; }
  .label--syrah .region { top: 254px; font-size: 19px; }
  .label--syrah .varietal { top: 290px; font-size: 54px; }
  .label--syrah .vintage { top: 378px; font-size: 10px; }
</style>
</head>
<body>
  <section class="label label--rose">
    <div class="wood-grain" role="img" aria-label="Light wood grain texture"></div>
    <div class="wordmark">HARROWGATE</div>
    <div class="subline"><span>VINEYARDS</span><span class="rule"></span></div>
    <div class="varietal">Rosé</div>
    <div class="region">Willamette Valley</div>
    <div class="vintage">ESTATE | 2023 | GROWN</div>
  </section>

  <section class="label label--syrah">
    <div class="wood-grain" role="img" aria-label="Dark wood grain texture"></div>
    <div class="wordmark">HARROWGATE</div>
    <div class="subline"><span class="rule"></span><span>VINEYARDS</span><span class="rule"></span></div>
    <div class="region">Willamette Valley</div>
    <div class="varietal">Syrah</div>
    <div class="vintage">ESTATE | 2023 | GROWN</div>
  </section>
</body>
</html>
```